Meditation for IVF and infertility

I need a flyer inviting IVF patients to join my Meditation class, I would like to offer free meditation to ivf women and for couples this class is free every Thursday night at 5 pm
2465 west halloran blvd suite K Santa Barbara Ca 93274
larkvale-meditation.com for more details

```html
<!DOCTYPE html>
<html lang="en">
<head>
<meta charset="utf-8">
<title>Larkvale Meditation – Free Meditation Flyer</title>
<link rel="stylesheet" href="https://fonts.googleapis.com/css2?family=Poppins:wght@400;500;600;700&display=swap">
<style>
  :root {
    --page-bg: #ecebe8;
    --paper: #ffffff;
    --ink: #454545;
    --ink-soft: #555555;
    --dark: #262626;
    --band: #5a5a5a;
    --pill-top: #8a8a8a;
    --pill-bottom: #3e3e3e;
    --photo-a: #dcd6cf;
    --photo-b: #b9b2aa;
    --photo-c: #6f6a66;
    --white: #ffffff;
  }
  * { margin: 0; padding: 0; box-sizing: border-box; }
  html, body {
    width: 1200px; height: 1200px; overflow: hidden;
    background: var(--page-bg);
    font-family: "Poppins", sans-serif;
  }
  .flyer {
    position: absolute; left: 202px; top: 40px;
    width: 795px; height: 1120px;
    background: var(--paper);
    box-shadow: 0 8px 30px rgba(0,0,0,0.18);
    overflow: hidden;
  }
  .flyer-art { position: absolute; inset: 0; width: 795px; height: 1120px; }
  .brand-name {
    position: absolute; left: 612px; top: 439px; transform: translate(-50%, -50%);
    width: 220px; text-align: center;
    font-weight: 600; color: var(--ink); font-size: 36px; line-height: 1.05;
  }
  .brand-name span { display: block; font-size: 18px; margin-top: 2px; padding-left: 60px; }
  .headline {
    position: absolute; left: 0; right: 0; top: 666px; text-align: center;
    font-weight: 700; font-size: 48px; color: var(--ink); letter-spacing: 0.5px;
  }
  .subline {
    position: absolute; left: 0; right: 0; top: 729px; text-align: center;
    font-weight: 400; font-size: 26px; color: var(--ink-soft);
  }
  .calendar-icon { position: absolute; left: 362px; top: 786px; width: 76px; height: 76px; }
  .schedule {
    position: absolute; left: 0; right: 0; top: 876px; text-align: center;
    color: var(--ink); line-height: 1;
  }
  .schedule-day { font-size: 26px; font-weight: 400; }
  .schedule-time { font-size: 44px; font-weight: 400; margin-top: 6px; }
  .schedule b { font-weight: 700; }
  .phone {
    position: absolute; left: 189px; top: 979px; width: 415px; height: 49px;
    display: flex; align-items: center; justify-content: center; gap: 10px;
    color: var(--white); font-weight: 700; font-size: 31px; letter-spacing: 1px;
  }
  .phone svg { width: 28px; height: 28px; }
  .contact-line {
    position: absolute; left: 0; right: 0; text-align: center;
    color: var(--white); display: flex; align-items: center; justify-content: center; gap: 14px;
  }
  .contact-line svg { width: 20px; height: 20px; }
  .web { top: 1046px; font-size: 16px; }
  .address { top: 1080px; font-size: 15px; }
</style>
</head>
<body>
<main class="flyer">
  <svg class="flyer-art" viewBox="0 0 1005 1413" preserveAspectRatio="none">
    <defs>
      <linearGradient id="photoTone" x1="0" y1="0" x2="0" y2="1">
        <stop offset="0" stop-color="var(--photo-a)"/>
        <stop offset="0.55" stop-color="var(--photo-b)"/>
        <stop offset="1" stop-color="var(--photo-c)"/>
      </linearGradient>
      <linearGradient id="pillTone" x1="0" y1="0" x2="0" y2="1">
        <stop offset="0" stop-color="var(--pill-top)"/>
        <stop offset="1" stop-color="var(--pill-bottom)"/>
      </linearGradient>
      <clipPath id="paperClip"><rect width="1005" height="1413"/></clipPath>
    </defs>
    <g clip-path="url(#paperClip)">
      <circle class="frame-ring" cx="432" cy="268" r="522" fill="var(--dark)"/>
      <circle class="frame-gap" cx="420" cy="254" r="503" fill="var(--paper)"/>
      <circle class="frame-line" cx="420" cy="254" r="496" fill="var(--band)"/>
      <circle class="photo-area" cx="418" cy="250" r="488" fill="url(#photoTone)"
              role="img" aria-label="Photo of a group of people meditating cross-legged in a bright studio"/>
    </g>
    <circle class="brand-badge" cx="774" cy="555" r="178" fill="var(--paper)"/>
    <circle class="brand-badge-line" cx="774" cy="555" r="157" fill="none" stroke="var(--ink)" stroke-width="3"/>
    <rect class="footer-stripe" x="0" y="1259" width="1005" height="18" fill="var(--band)"/>
    <rect class="footer-band" x="0" y="1275" width="1005" height="138" fill="var(--dark)"/>
    <rect class="phone-pill" x="239" y="1238" width="525" height="62" rx="31" fill="url(#pillTone)" stroke="var(--white)" stroke-width="3"/>
  </svg>

  <div class="brand-name">Larkvale<span>Meditation</span></div>

  <h1 class="headline">FREE MEDITATION</h1>
  <p class="subline">To ivf women and for couples this class</p>

  <svg class="calendar-icon" viewBox="0 0 76 76" fill="none" stroke="var(--ink)" stroke-width="2.2">
    <rect x="3" y="10" width="60" height="56" rx="4"/>
    <line x1="3" y1="22" x2="63" y2="22"/>
    <rect x="12" y="4" width="5" height="10" rx="2"/>
    <rect x="25" y="4" width="5" height="10" rx="2"/>
    <rect x="38" y="4" width="5" height="10" rx="2"/>
    <rect x="51" y="4" width="5" height="10" rx="2"/>
    <rect x="11" y="29" width="7" height="6"/><rect x="23" y="29" width="7" height="6"/>
    <rect x="35" y="29" width="7" height="6"/><rect x="47" y="29" width="7" height="6"/>
    <rect x="11" y="41" width="7" height="6"/><rect x="23" y="41" width="7" height="6"/>
    <rect x="35" y="41" width="7" height="6"/>
    <rect x="11" y="53" width="7" height="6"/><rect x="23" y="53" width="7" height="6"/>
    <circle cx="60" cy="60" r="13" fill="var(--paper)"/>
    <polyline points="60,52 60,60 55,65"/>
  </svg>

  <div class="schedule">
    <p class="schedule-day">EVERY <b>THURSDAY NIGHT</b> AT</p>
    <p class="schedule-time"><b>5 PM</b> FREE CLASS</p>
  </div>

  <div class="phone">
    <svg viewBox="0 0 28 28"><circle cx="14" cy="14" r="14" fill="var(--white)"/>
      <path d="M10 7c1 0 2 3 2 4s-2 1.5-1.5 2.5 2.5 3.5 3.5 4 1.5-1.5 2.5-1.5 4 1 4 2-1.5 3-3.5 3C12 21 7 16 7 10c0-2 2-3 3-3z" fill="var(--pill-bottom)"/></svg>
    707-555-0148
  </div>

  <p class="contact-line web">
    <svg viewBox="0 0 20 20" fill="none" stroke="var(--white)" stroke-width="1.5"><circle cx="10" cy="10" r="8.5"/><ellipse cx="10" cy="10" rx="4" ry="8.5"/><line x1="1.5" y1="10" x2="18.5" y2="10"/><line x1="3" y1="5.5" x2="17" y2="5.5"/><line x1="3" y1="14.5" x2="17" y2="14.5"/></svg>
    larkvale-meditation.com
  </p>
  <p class="contact-line address">
    <svg viewBox="0 0 20 20"><circle cx="10" cy="10" r="10" fill="var(--white)"/><path d="M10 4a4 4 0 0 1 4 4c0 3-4 8-4 8s-4-5-4-8a4 4 0 0 1 4-4z" fill="none" stroke="var(--dark)" stroke-width="1.5"/><circle cx="10" cy="8" r="1.5" fill="var(--dark)"/></svg>
    2465 west halloran blvd suite K Santa Barbara Ca 93274
  </p>
</main>
</body>
</html>
```